The title of the book is: Resonant Foundations for Builders
I need a front and back cover for my new book.
This is a reference book written to teach architects the basics of acoustics and sound.
The subtitle is: The handbook on echoes and noise most designers hoped their teachers had covered in class
Author is: Daniel Orwick
Publisher: TLBW Press
Primary colors desired are deep red, and deep rich gold. A splash of cobalt blue might be nice too.
Black and/or White fonts
I'm a fan of art deco designs, but I'm also a minimalist, so I'd like something that's not too busy.
This will be used for both a paperback and ebook. Format for "portrait" viewing.
Final files need to be high-res .jpg. Size: 1873 pixels on the longest side, 1600 pixels on the shortest side (350 dpi)
The inside cover page is attached as a reference only.

Target Market(s)

Architects

Industry/Entity Type

Architecture, interior design, and pro audio

Font styles to use
Sans Serif
Other font styles liked:
• Arial

Colors
0054AA
0677BA
7BADD7
CADEEF
E8F1F8
FFC000
F8CF3A
FAE287
FDF2CF
FEFAEE
EB3D1F
EC4F4E
F09395
F8D3D4
FCEDEE

Requirements
Must have
• Elegant font cover design
Nice to have
• Spine and back cover design to compliment front cover. Spine will be roughly 1/2"
Should not have
• Anything that will date the book based on front cover graphics

```html
<!DOCTYPE html>
<html lang="en">
<head>
<meta charset="utf-8">
<title>Resonant Foundations for Builders — Cover</title>
<link rel="stylesheet" href="https://fonts.googleapis.com/css2?family=Arimo:ital,wght@0,400;0,700;1,700&family=Noto+Serif:wght@400&display=swap">
<style>
  :root {
    --deep-red: #b32a1c;
    --soft-red: #c0301f;
    --white: #ffffff;
    --black: #000000;
    --gold: #f8cf3a;
    --cyan: #18b6d8;
    --slate: #3a5a78;
    --violet: #a955ad;
    --magenta: #a41f56;
  }
  html, body {
    margin: 0;
    padding: 0;
    width: 1025px;
    height: 1200px;
    overflow: hidden;
    background: var(--white);
  }
  .cover {
    position: relative;
    width: 1025px;
    height: 1200px;
    background: var(--deep-red);
    overflow: hidden;
    font-family: "Arimo", Arial, sans-serif;
    color: var(--white);
  }
  .cover-art {
    position: absolute;
    inset: 0;
    width: 1025px;
    height: 1200px;
  }
  .title {
    position: absolute;
    inset: 0;
    margin: 0;
    font-weight: 700;
    line-height: 1;
  }
  .title-line {
    position: absolute;
    white-space: nowrap;
  }
  .title .initial { font-size: 157px; }
  .title .small-caps { font-size: 92px; letter-spacing: 1px; }
  .title-line--first { left: 102px; top: 80px; }
  .title-line--second { left: 106px; top: 248px; }
  .title-line--second .initial { font-size: 127px; }
  .title-line--for {
    left: 302px;
    top: 388px;
    font-size: 62px;
  }
  .title-line--builders {
    left: 136px;
    top: 468px;
    font-size: 126px;
    font-weight: 400;
  }
  .subtitle {
    position: absolute;
    left: 60px;
    width: 905px;
    top: 610px;
    margin: 0;
    font-family: "Noto Serif", Georgia, serif;
    font-size: 31px;
    line-height: 43px;
    letter-spacing: 1.2px;
    text-align: center;
  }
  .publisher-band {
    position: absolute;
    left: 0;
    top: 988px;
    width: 1025px;
    height: 55px;
    background: var(--white);
  }
  .author-band {
    position: absolute;
    left: 0;
    top: 1043px;
    width: 1025px;
    height: 157px;
    background: var(--black);
  }
  .publisher-name {
    position: absolute;
    left: 160px;
    top: 1000px;
    margin: 0;
    font-family: "Noto Serif", Georgia, serif;
    font-size: 26px;
    line-height: 32px;
    color: var(--black);
  }
  .author {
    position: absolute;
    left: 0;
    width: 1025px;
    top: 1100px;
    margin: 0;
    text-align: center;
    padding-left: 12px;
    box-sizing: border-box;
    font-size: 48px;
    font-weight: 700;
    font-style: italic;
    color: var(--gold);
  }
</style>
</head>
<body>
<main class="cover">
  <svg class="cover-art" viewBox="0 0 1025 1200" xmlns="http://www.w3.org/2000/svg">
    <defs>
      <radialGradient id="instrument-glow" cx="0.62" cy="0.38" r="0.6">
        <stop offset="0" stop-color="var(--soft-red)"/>
        <stop offset="0.7" stop-color="var(--soft-red)" stop-opacity="0.6"/>
        <stop offset="1" stop-color="var(--deep-red)" stop-opacity="0"/>
      </radialGradient>
      <linearGradient id="wave-tones" x1="0" y1="0" x2="1" y2="0">
        <stop offset="0" stop-color="var(--violet)"/>
        <stop offset="0.2" stop-color="var(--magenta)"/>
        <stop offset="0.38" stop-color="var(--deep-red)"/>
        <stop offset="0.6" stop-color="var(--cyan)"/>
        <stop offset="0.78" stop-color="var(--slate)"/>
        <stop offset="1" stop-color="var(--cyan)"/>
      </linearGradient>
      <linearGradient id="wave-fade" x1="0" y1="0" x2="0" y2="1">
        <stop offset="0" stop-color="#fff" stop-opacity="0"/>
        <stop offset="1" stop-color="#fff" stop-opacity="1"/>
      </linearGradient>
      <mask id="wave-mask">
        <rect x="0" y="850" width="1025" height="138" fill="url(#wave-fade)"/>
      </mask>
    </defs>

    <rect class="instrument-area" role="img" aria-label="Soft illustration of an acoustic guitar body with strings, sound hole and bridge"
          x="540" y="0" width="485" height="640" fill="url(#instrument-glow)"/>

    <rect class="sound-wave-area" role="img" aria-label="Colourful abstract sound wave hills along the lower edge"
          x="0" y="850" width="1025" height="138" fill="url(#wave-tones)" mask="url(#wave-mask)"/>
  </svg>

  <h1 class="title" aria-label="Resonant Foundations for Builders">
    <span class="title-line title-line--first"><span class="initial">R</span><span class="small-caps">ESONANT</span></span>
    <span class="title-line title-line--second"><span class="initial">F</span><span class="small-caps">OUNDATIONS</span></span>
    <span class="title-line title-line--for">FOR</span>
    <span class="title-line title-line--builders">BUILDERS</span>
  </h1>

  <p class="subtitle">The handbook on echoes and noise most designers hoped their teachers had covered in class</p>

  <div class="publisher-band"></div>
  <div class="author-band"></div>
  <p class="publisher-name">TLBW Press</p>

  <p class="author">Daniel Orwick</p>
</main>
</body>
</html>
```